Used Semi Truck Website Redesign

We are redoing the website backend and would like to also do a front end redesign. I would like a Mobile and Desktop mockup for each page. The website has more mobile visitors than desktop visitors. Our competitor is http://www.haulwaymarketbay.example. We don't want to copy them exactly but we want a site that looks more like that. We need the functionality of that site. One big difference is that we also sell parts and trailers.

We need a redesign for front page, product detail page, search result page, content page. It is very important that the site is very easy to use on mobile devices. Our target audience is Truck drivers.

Feel free to use demo fonts stock images, and icons. We will purchase necessary 3rd party media when a winner is chosen.

Target Market(s)

People who want to buy used trucks.

Coding

Coded - Design and coding required

Number of Pages Required

5+ page

Requirements
Must have
• Mockup for Desktop and Mobile pages.

```html
<!DOCTYPE html>
<html lang="en">
<head>
<meta charset="utf-8">
<title>Truck Detail</title>
<link href="https://fonts.googleapis.com/css2?family=Roboto:wght@300;400;500&family=Roboto+Mono:wght@400&display=swap" rel="stylesheet">
<style>
:root{
  --red:#ee1c25;
  --red-dark:#c8141c;
  --ink:#222;
  --muted:#666;
  --dark:#1f2128;
  --footer:#23252c;
  --panel:#eeeef2;
  --line:#dcdce0;
  --white:#fff;
}
*{margin:0;padding:0;box-sizing:border-box}
html,body{width:787px;height:1200px;overflow:hidden}
body{font-family:'Roboto',Arial,sans-serif;color:var(--ink);background:var(--white);position:relative;font-size:8px}
.abs{position:absolute}
.topbar{left:0;top:0;width:787px;height:34px;background:var(--dark)}
.logo{left:58px;top:9px;color:#fff;font-size:12px;font-weight:500;letter-spacing:.5px}
.logo span{color:var(--red);font-family:'Roboto Mono',monospace;font-weight:400}
.nav{top:13px;font-size:8px;color:#aaa}
.nav.active{color:#fff}
.nav-active-bar{left:291px;top:0;width:20px;height:2px;background:#fff}
.nav-sep{left:374px;top:12px;width:1px;height:10px;background:#555}
.social{top:13px;width:8px;height:8px;border-radius:50%;background:#ddd}
.hero{left:0;top:34px;width:787px;height:129px;background:linear-gradient(90deg,#2b2f3a,#454a55 45%,#2a2d36)}
.hero-title{left:0;width:787px;top:72px;text-align:center;color:#fff;font-size:14.5px;font-weight:300}
.hero-btn{top:98px;height:26px;line-height:26px;text-align:center;color:#fff;font-size:8.5px;background:rgba(255,255,255,.18)}
.hero-btn.sell{background:var(--red)}
.searchbar{left:0;top:163px;width:787px;height:41px;background:var(--red)}
.field{top:163px;height:41px;line-height:41px;color:#fff;font-size:8.5px;font-weight:500;border-right:1px solid rgba(255,255,255,.25)}
.field .chev{position:absolute;right:10px;top:0;font-size:7px}
.search-btn{left:694px;top:163px;width:35px;height:41px;background:var(--red-dark)}
.content-bg{left:0;top:204px;width:494px;height:784px;background:var(--panel)}
.tab{top:220px;font-size:8.5px;color:var(--muted)}
.tab.active{color:var(--ink)}
.tab-line{left:0;top:240px;width:494px;height:1px;background:var(--line)}
.tab-under{left:58px;top:239px;width:27px;height:2px;background:var(--red)}
.photo{left:58px;top:258px;width:411px;height:191px;background:linear-gradient(160deg,#1a1a1e,#4a3a2c 40%,#6a5a48 55%,#1c1c22)}
.share{left:438px;top:264px;width:24px;height:24px;border-radius:50%;background:#fff}
.dot{top:405px;width:26px;height:26px;border-radius:50%}
.price{left:57px;top:469px;color:var(--red);font-size:13px;font-weight:500}
.spec-box{left:58px;top:501px;width:411px;height:208px;background:#fff}
.spec-tab{top:517px;font-size:8.5px;color:var(--muted)}
.spec-tab.active{color:var(--ink)}
.spec-line{left:58px;top:540px;width:411px;height:1px;background:#e6e6ea}
.spec-under{left:80px;top:539px;width:51px;height:2px;background:var(--red)}
.spec-row{left:81px;font-size:8px;font-weight:400;color:var(--ink)}
.spec-row span{position:absolute;left:67px;color:var(--muted);white-space:nowrap}
.h2{font-size:12.5px;color:var(--ink);font-weight:400}
.rule{width:26px;height:1px;background:#bbb}
.desc{left:57px;top:763px;width:412px;font-size:8px;line-height:14.5px;color:#444}
.card{background:#fff;border:1px solid #e4e4e8}
.label{font-size:7.3px;color:#555}
.in-line{left:536px;width:181px;height:1px;background:#ddd}
.captcha{left:537px;top:552px;width:128px;height:48px;background:linear-gradient(90deg,#f2f2f2,#d0d0d0,#eeeeee)}
.send{left:536px;top:636px;width:177px;height:26px;background:var(--red);color:#fff;text-align:center;line-height:26px;font-size:8px}
.thumb{left:536px;width:72px;height:50px}
.sim{left:619px;font-size:8px;line-height:13px;color:#333}
.sim b{display:block;color:var(--red);font-size:10px;font-weight:500;margin-top:2px}
.footer{left:0;top:988px;width:787px;height:182px;background:var(--footer)}
.f-h{top:1019px;color:#fff;font-size:10px;font-weight:500}
.f-item{font-size:7.3px;line-height:12.8px;color:#bbb;width:200px}
.f-item b{display:block;color:#fff;font-weight:500;font-size:7px}
.f-item::before{content:"";position:absolute;left:1px;top:4px;width:5px;height:5px;background:#ccc}
.f-sep{height:1px;background:#3a3c44}
.f-link{font-size:7.3px;color:#bbb}
.bottombar{left:0;top:1170px;width:787px;height:30px;background:var(--red)}
.b-text{top:1181px;color:#fff;font-size:7.3px}
.to-top{left:745px;top:975px;width:26px;height:26px;border-radius:50%;background:var(--red)}
</style>
</head>
<body>
<header>
  <div class="abs topbar"></div>
  <div class="abs logo">Logo <span>here</span></div>
  <div class="abs nav-active-bar"></div>
  <div class="abs nav active" style="left:291px">Login</div>
  <div class="abs nav" style="left:328px">Register</div>
  <div class="abs nav-sep"></div>
  <div class="abs nav" style="left:386px">Find a dealer</div>
  <div class="abs nav" style="left:450px">Dealer Login</div>
  <div class="abs social" style="left:632px" aria-label="Social link"></div>
  <div class="abs social" style="left:654px" aria-label="Social link"></div>
  <div class="abs social" style="left:677px" aria-label="Social link"></div>
  <div class="abs social" style="left:699px" aria-label="Social link"></div>
  <div class="abs social" style="left:720px" aria-label="Social link"></div>

  <div class="abs hero" role="img" aria-label="Dark industrial truck yard backdrop"></div>
  <div class="abs hero-title">Truck name here, USA</div>
  <div class="abs hero-btn" style="left:317px;width:49px">Find</div>
  <div class="abs hero-btn sell" style="left:370px;width:48px">Sell</div>
  <div class="abs hero-btn" style="left:422px;width:49px">Research</div>

  <div class="abs searchbar"></div>
  <div class="abs field" style="left:0;width:182px;padding-left:58px">Keywords</div>
  <div class="abs field" style="left:182px;width:140px;padding-left:16px">Select a class<span class="chev">&#8964;</span></div>
  <div class="abs field" style="left:322px;width:140px;padding-left:16px">Select a category<span class="chev">&#8964;</span></div>
  <div class="abs field" style="left:462px;width:94px;padding-left:16px">Zip code</div>
  <div class="abs field" style="left:556px;width:138px;padding-left:15px;border-right:0">Any Distance<span class="chev">&#8964;</span></div>
  <div class="abs search-btn">
    <svg width="35" height="41" viewBox="0 0 35 41"><circle cx="16.5" cy="19.5" r="4.5" fill="none" stroke="#fff" stroke-width="1.2"/><line x1="19.8" y1="22.8" x2="23" y2="26" stroke="#fff" stroke-width="1.2"/></svg>
  </div>
</header>

<main>
  <div class="abs content-bg"></div>
  <div class="abs tab active" style="left:58px">Details</div>
  <div class="abs tab" style="left:107px">Shipping Quote</div>
  <div class="abs tab" style="left:189px">Inspection request</div>
  <div class="abs tab" style="left:284px">Finance</div>
  <div class="abs tab-line"></div>
  <div class="abs tab-under"></div>

  <div class="abs photo" role="img" aria-label="Night street with a truck, lit shop signs"></div>
  <div class="abs share">
    <svg width="24" height="24" viewBox="0 0 24 24"><g fill="none" stroke="#444" stroke-width=".9"><circle cx="14.5" cy="8.5" r="1.8"/><circle cx="14.5" cy="15.5" r="1.8"/><circle cx="9" cy="12" r="1.8"/><line x1="10.6" y1="11" x2="13" y2="9.4"/><line x1="10.6" y1="13" x2="13" y2="14.6"/></g></svg>
  </div>
  <div class="abs dot" style="left:215px;background:var(--red)"></div>
  <div class="abs dot" style="left:251px;background:#8a8e96"></div>
  <div class="abs dot" style="left:287px;background:#6a7a9a"></div>

  <div class="abs price">Price: $75,000</div>

  <div class="abs spec-box"></div>
  <div class="abs spec-tab active" style="left:80px">Specification</div>
  <div class="abs spec-tab" style="left:153px">Seller Information</div>
  <div class="abs spec-line"></div>
  <div class="abs spec-under"></div>
  <div class="abs spec-row" style="top:552px">Year:<span>2015</span></div>
  <div class="abs spec-row" style="top:570px">Make:<span>Other</span></div>
  <div class="abs spec-row" style="top:587px">Model:<span>OTHER</span></div>
  <div class="abs spec-row" style="top:605px">Class:<span>TRAILER</span></div>
  <div class="abs spec-row" style="top:622px">Category:<span>Double Drop Trailer</span></div>
  <div class="abs spec-row" style="top:640px">New/Used:<span>Used</span></div>
  <div class="abs spec-row" style="top:657px">VIN:<span>453523jkr324j35431</span></div>
  <div class="abs spec-row" style="top:675px">Price:<span>75000</span></div>

  <div class="abs h2" style="left:58px;top:727px">Description</div>
  <div class="abs rule" style="left:58px;top:750px"></div>
  <p class="abs desc">dolor sit amet consectetuer adipiscing elit aenean commodo ligula eget dolor aenean massa cum sociis natoque penatibus et magnis dis parturient montes, nascetur ridiculus mus donec quam felis ultricies nec pellentesque eu pretium quis sem nulla consequat massa quis enim donec pede justo fringilla vel aliquet nec vulputate eget arcu in enim justo rhoncus ut imperdiet.</p>

  <aside>
    <div class="abs card" style="left:520px;top:228px;width:209px;height:446px"></div>
    <div class="abs h2" style="left:536px;top:246px">Contact Seller</div>
    <div class="abs rule" style="left:536px;top:267px"></div>
    <div class="abs label" style="left:536px;top:280px"><span style="color:#888">Seller:</span> Private</div>
    <div class="abs label" style="left:536px;top:293px;color:#333">Hello, I'm interested in your 2015 other Stock no.</div>
    <div class="abs label" style="left:537px;top:319px">Your Convenient time</div>
    <div class="abs label" style="left:708px;top:317px">&#8964;</div>
    <div class="abs in-line" style="top:334px"></div>
    <div class="abs label" style="left:537px;top:354px">Enter phone number</div>
    <div class="abs in-line" style="top:369px"></div>
    <div class="abs label" style="left:537px;top:389px">Enter email address</div>
    <div class="abs in-line" style="top:404px"></div>
    <div class="abs label" style="left:537px;top:424px">Comments</div>
    <div class="abs in-line" style="top:463px"></div>
    <div class="abs label" style="left:537px;top:482px">Thank you,</div>
    <div class="abs in-line" style="top:498px"></div>
    <div class="abs" style="left:536px;top:517px;width:7px;height:7px;background:#ddd"></div>
    <div class="abs label" style="left:549px;top:515px;width:160px;line-height:12.8px;font-size:7.8px">Would you like to get our newsletter and special offers via email?</div>
    <div class="abs captcha" role="img" aria-label="Security code image"></div>
    <div class="abs label" style="left:537px;top:608px">Enter code</div>
    <div class="abs in-line" style="top:624px"></div>
    <div class="abs send">Send</div>

    <div class="abs card" style="left:520px;top:687px;width:209px;height:274px"></div>
    <div class="abs h2" style="left:536px;top:705px">Find Similar Trucks</div>
    <div class="abs thumb" style="top:741px;background:linear-gradient(135deg,#9aa0a8,#3a3c40 60%,#c04030)" role="img" aria-label="Tow truck photo"></div>
    <div class="abs sim" style="top:745px">Similar truck name here.<br>Truck category.<b>$45.8K</b></div>
    <div class="abs thumb" style="top:817px;background:linear-gradient(180deg,#8a8478,#c8b8a0 50%,#3a3630)" role="img" aria-label="Off-road vehicle photo"></div>
    <div class="abs sim" style="top:821px">Similar truck name here.<br>Truck category.<b>$41.1K</b></div>
    <div class="abs thumb" style="top:893px;background:linear-gradient(180deg,#3a6ab0,#5a8a40 55%,#6a5a3a)" role="img" aria-label="Pickup truck in a yard photo"></div>
    <div class="abs sim" style="top:897px">Similar truck name here.<br>Truck category.<b>$35.5K</b></div>
  </aside>
</main>

<footer>
  <div class="abs footer"></div>
  <div class="abs to-top">
    <svg width="26" height="26" viewBox="0 0 26 26"><path d="M13 17V9M10 12l3-3 3 3" fill="none" stroke="#fff" stroke-width="1"/></svg>
  </div>
  <div class="abs f-h" style="left:58px">Our Blogs</div>
  <div class="abs f-item" style="left:58px;top:1048px;padding-left:10px;width:205px">Dictum nullam felis eu pede mollis pretium integer tincidunt cras dapibus vivamus elementum semper.<b>10-Dec-2016</b></div>
  <div class="abs f-sep" style="left:58px;top:1094px;width:200px"></div>
  <div class="abs f-item" style="left:58px;top:1106px;padding-left:10px;width:210px">Dec dictum felis eu pede mollis pretium integer tincidunt cras dapibus vivamus elementum semper dipsum.<b>10-Dec-2016</b></div>

  <div class="abs f-h" style="left:307px">Chirpline</div>
  <div class="abs f-item" style="left:307px;top:1048px;padding-left:10px;width:205px">Nullam dictum felis eu pede mollis pretium integer tincidunt cras dapibus vivamus elementum semper.<b>Reshare</b></div>
  <div class="abs f-sep" style="left:307px;top:1094px;width:200px"></div>
  <div class="abs f-item" style="left:307px;top:1106px;padding-left:10px;width:205px">Lorem dictum felis eu pede mollis pretium integer tincidunt cras dapibus vivamus elementum sem ipsum.<b>Reshare</b></div>

  <div class="abs f-h" style="left:553px">Resource Advertisers</div>
  <div class="abs f-link" style="left:553px;top:1050px">› Insurance</div>
  <div class="abs f-link" style="left:553px;top:1069px">› Jobs &amp; Training</div>
  <div class="abs f-link" style="left:553px;top:1087px">› Vehicle History</div>
  <div class="abs f-link" style="left:553px;top:1106px">› Truck Bodies</div>
  <div class="abs f-link" style="left:553px;top:1125px">› Finance/Lease</div>
  <div class="abs f-link" style="left:640px;top:1050px">› Truck Parts</div>
  <div class="abs f-link" style="left:640px;top:1069px">› Steel Buildings</div>
  <div class="abs f-link" style="left:640px;top:1087px">› Fuel Management</div>
  <div class="abs f-link" style="left:640px;top:1106px">› Shipping &amp; Transport</div>
  <div class="abs f-link" style="left:640px;top:1125px">› View All</div>

  <div class="abs bottombar"></div>
  <div class="abs b-text" style="left:58px">© Company name here, All Rights Reserved.</div>
  <div class="abs b-text" style="left:568px">Trucks for sale</div>
  <div class="abs b-text" style="left:637px">New Arrivals</div>
  <div class="abs b-text" style="left:699px">Site map</div>
</footer>
</body>
</html>
```